BRASKETT LAND SERVICES BILLBOARD DESIGN

I NEED A BILLBOARD FOR MY BUSINESS. WE ARE A LAND CLEARING COMPANY AND I WOULD LIKE TO ADD A PICTURE OF MY TRACK LOADER TO THE SIGN. OPEN TO COLORS. I WOULD ALSO LIKE TO HAVE MY PHONE NUMBER 555-284-7196, WEBSITE WWW.BRASKETTLANDSERVICES.EXAMPLE, AND EMAIL ON THE SIGN (CONTACT@BRASKETTLANDSERVICES.EXAMPLE). DESIGNERS CAN HAVE THE FREEDOM TO DO WHATEVER STYLE THEY WANT AND TO USE ANY COLORS THEY WANT.

Target Market(s)

ANYONE WITH PROPERTY

Requirements
Must have
• PICTURE OF TRACK LOADER, WEBSITE, PHONE NUMBER, EMAIL
Nice to have
• OPEN TO ANYTHING
Should not have
• OPEN TO ANYTHING

```html
<!DOCTYPE html>
<html lang="en">
<head>
<meta charset="utf-8">
<title>Braskett Land Services Billboard</title>
<link rel="stylesheet" href="https://fonts.googleapis.com/css2?family=Montserrat:wght@600;700;900&display=swap">
<style>
  :root {
    --page: #e9eaec;
    --paper: #ffffff;
    --ink: #111111;
    --night: #1f1609;
    --swoosh: #3b3133;
    --alert: #d3141c;
    --navy: #1b2b5e;
    --machine-hot: #e8562a;
    --machine-dark: #2a2622;
  }
  * { box-sizing: border-box; margin: 0; padding: 0; }
  html, body { width: 1200px; height: 900px; overflow: hidden; }
  body {
    background: var(--page);
    font-family: "Montserrat", sans-serif;
    display: flex; align-items: center; justify-content: center;
  }
  .billboard {
    position: relative;
    width: 1120px; height: 530px;
    background: var(--paper);
    overflow: hidden;
    box-shadow: 0 10px 30px rgba(0,0,0,.18);
  }
  .backdrop { position: absolute; inset: 0; }
  .loader-photo {
    position: absolute;
    left: 450px; top: 120px; width: 640px; height: 330px;
    border-radius: 30px 60px 90px 40px;
    background: linear-gradient(120deg, var(--machine-dark) 0%, #6b645c 30%, var(--machine-hot) 60%, #c9471f 85%, var(--machine-dark) 100%);
  }
  .brand-name {
    position: absolute; left: 40px; top: 100px;
    width: 390px;
    font-weight: 900; font-size: 60px; line-height: 1.02;
    color: var(--ink); letter-spacing: 0;
  }
  .call-now {
    position: absolute; left: 52px; top: 360px;
    width: 330px; height: 70px; border-radius: 35px;
    background: var(--ink); color: var(--paper);
    font-weight: 700; font-size: 44px;
    display: flex; align-items: center; justify-content: center;
  }
  .phone {
    position: absolute; left: 52px; top: 440px;
    display: flex; align-items: center; gap: 10px;
    color: var(--alert); font-weight: 700; font-size: 46px;
  }
  .contact-list {
    position: absolute; left: 560px; top: 462px;
    list-style: none; color: var(--navy);
    font-weight: 600; font-size: 19px; letter-spacing: 1.6px;
  }
  .contact-list li { display: flex; align-items: center; gap: 14px; height: 32px; }
  .contact-list svg { flex: none; }
</style>
</head>
<body>
  <main class="billboard">
    <svg class="backdrop" width="1120" height="530" viewBox="0 0 1120 530" aria-hidden="true">
      <path d="M350,0 C410,190 500,340 690,410 C850,465 1000,462 1120,452 L1120,0 Z" fill="var(--swoosh)"/>
      <path d="M440,0 C490,170 570,320 730,390 C870,440 1010,440 1120,430 L1120,0 Z" fill="var(--night)"/>
    </svg>

    <div class="loader-photo" role="img" aria-label="Photo of an orange compact track loader fitted with a forestry mulcher attachment"></div>

    <h1 class="brand-name">BRASKETT<br>LAND<br>SERVICES</h1>

    <div class="call-now">CALL NOW!</div>

    <div class="phone">
      <svg width="30" height="38" viewBox="0 0 30 38" aria-hidden="true">
        <rect x="0" y="0" width="30" height="38" rx="5" fill="var(--alert)"/>
        <path d="M11,8 l4,0 l1,6 l-3,2 c1,3 3,6 5,7 l2,-3 l5,2 l0,5 c-9,1 -17,-9 -14,-19 z" fill="var(--paper)"/>
      </svg>
      <span>555-284-7196</span>
    </div>

    <ul class="contact-list">
      <li>
        <svg width="30" height="30" viewBox="0 0 30 30" aria-hidden="true" fill="none" stroke="var(--navy)" stroke-width="1.8">
          <circle cx="15" cy="15" r="13"/><ellipse cx="15" cy="15" rx="6" ry="13"/>
          <line x1="2" y1="15" x2="28" y2="15"/><line x1="4" y1="8" x2="26" y2="8"/><line x1="4" y1="22" x2="26" y2="22"/>
        </svg>
        <span>www.braskettlandservices.example</span>
      </li>
      <li>
        <svg width="30" height="20" viewBox="0 0 30 20" aria-hidden="true">
          <rect x="0" y="0" width="30" height="20" rx="2" fill="var(--navy)"/>
          <path d="M1,1 L15,12 L29,1" fill="none" stroke="var(--paper)" stroke-width="2"/>
        </svg>
        <span>contact@braskettlandservices.example</span>
      </li>
    </ul>
  </main>
</body>
</html>
```